Etiketten-Design für Weinflasche
Sehr gute Zusammenarbeit bei Tag und Nacht, sehr kooperativ ,flexibel und entgegenkommend. Empfehlenswert
Zielgruppe
Weinbau - Eigenbau Wein -Weinverkauf
Aufgabenstellung
Bräuchte oder Suche ein Flaschenetikette für Rotwein der Marke Zweigelt Das Ausmaß der Etikette sollte 8cm Breit und 12cm Hoch sein. Habe meine letzte Etikette beigelegt sie Anhang

```html
<!DOCTYPE html>
<html lang="de">
<head>
<meta charset="utf-8">
<title>Zweigelt 2020 – Weinetikett</title>
<link rel="stylesheet" href="https://fonts.googleapis.com/css2?family=Crimson+Pro:wght@400&family=Jost:wght@400&display=swap">
<style>
  :root {
    --page: #ffffff;
    --label: #1f1f21;
    --wine-red: #a51430;
    --slate: #3e3e40;
    --mark: #111111;
  }
  html, body {
    margin: 0;
    padding: 0;
    width: 1200px;
    height: 1200px;
    overflow: hidden;
    background: var(--page);
  }
  .sheet {
    position: relative;
    width: 1200px;
    height: 1200px;
  }
  .crop-marks {
    position: absolute;
    inset: 0;
  }
  .label {
    position: absolute;
    left: 344px;
    top: 161px;
    width: 512px;
    height: 878px;
    background: var(--label);
    color: var(--wine-red);
    font-family: "Crimson Pro", Georgia, serif;
    font-weight: 400;
  }
  .label > * {
    position: absolute;
    left: 0;
    right: 0;
    margin: 0;
    text-align: center;
    line-height: 1;
  }
  .label__estate {
    top: 48px;
    font-size: 30px;
    letter-spacing: 1px;
  }
  .label__producer {
    top: 268px;
    font-size: 30px;
    letter-spacing: 0.5px;
  }
  .label__variety {
    top: 470px;
    font-size: 88px;
    letter-spacing: 1px;
  }
  .label__region-map {
    left: 222px;
    right: auto;
    top: 657px;
    width: 72px;
    height: 131px;
    background: var(--slate);
    border-radius: 30px 30px 20px 20px / 50px 50px 40px 40px;
  }
  .label__vintage {
    top: 806px;
    font-family: "Jost", Arial, sans-serif;
    font-size: 32px;
    letter-spacing: 2px;
  }
</style>
</head>
<body>
<main class="sheet">
  <svg class="crop-marks" width="1200" height="1200" viewBox="0 0 1200 1200" aria-hidden="true">
    <g stroke="var(--mark)" stroke-width="2.5">
      <line x1="344" y1="79" x2="344" y2="149"/>
      <line x1="856" y1="79" x2="856" y2="149"/>
      <line x1="344" y1="1059" x2="344" y2="1129"/>
      <line x1="856" y1="1059" x2="856" y2="1129"/>
      <line x1="259" y1="161" x2="329" y2="161"/>
      <line x1="871" y1="161" x2="941" y2="161"/>
      <line x1="259" y1="1039" x2="329" y2="1039"/>
      <line x1="871" y1="1039" x2="941" y2="1039"/>
    </g>
  </svg>

  <article class="label">
    <p class="label__estate">WEINBAU</p>
    <p class="label__producer">TOBIAS LOMANDER</p>
    <h1 class="label__variety">ZWEIGELT</h1>
    <div class="label__region-map" role="img" aria-label="Umrisskarte der Weinbauregion"></div>
    <p class="label__vintage">2020</p>
  </article>
</main>
</body>
</html>
```